BRENSDALE ELECTRICAL

all black background with silver and lime writing, fonts i like are gothic style but am open to ideas, will need a picture logo aswell as im putting this on my van.i am a electrical contractor starting up my own electrical business. underneath brensdale electrical heading on card we could put" professiona cost effective soloutions to all your electrical needs".{ or something of that nature }.on aback of card on top half list servises provided, real estate and commercial maintenance, new home and renovation rewires and upgrades, split system air conditioning, floor heat, tv phone data, smoke detoctors, lighting systems , builders welcome, , and also a thankyou for your business.

Real Estate

GERALD PILWORTHY
brensdaleelectrical@mailvox.com.au
0417302951
lic no 58120
ac lic no l293417
abn 37216058814

```html
<!DOCTYPE html>
<html lang="en">
<head>
<meta charset="utf-8">
<title>Brensdale Electrical — Business Card</title>
<link rel="stylesheet" href="https://fonts.googleapis.com/css2?family=Old+Standard+TT:ital,wght@0,400;0,700;1,400&family=Open+Sans:wght@400;700&display=swap">
<style>
  :root {
    --stage: #6e6f72;
    --card: #000000;
    --lime: #39e42a;
    --silver-light: #e8e8e8;
    --silver-mid: #a9a9a9;
    --silver-dark: #5c5c5c;
    --text-silver: #d9d9d9;
  }
  * { box-sizing: border-box; margin: 0; padding: 0; }
  html, body {
    width: 1200px; height: 1200px; overflow: hidden;
    background: var(--stage);
  }
  .card {
    position: absolute; left: 227px; width: 767px; height: 460px;
    background: var(--card); overflow: hidden;
    box-shadow: 0 14px 22px rgba(0,0,0,.45);
  }
  .card--front { top: 58px; }
  .card--back { top: 649px; }

  .brand {
    position: absolute; left: 85px; top: 48px;
    display: flex; align-items: center; gap: 18px;
  }
  .brand__mark {
    width: 40px; height: 40px; border-radius: 50%;
    background: var(--silver-mid);
  }
  .brand__name {
    font-family: "Old Standard TT", serif; font-weight: 400;
    font-size: 44px; color: var(--text-silver); line-height: 1;
  }
  .tagline {
    position: absolute; left: 190px; top: 106px;
    font-family: "Old Standard TT", serif; font-style: italic;
    font-size: 26px; color: var(--lime);
  }
  .glow {
    position: absolute; left: 120px; right: 60px; top: 150px; height: 30px;
    background: radial-gradient(ellipse at center, rgba(200,200,200,.35), rgba(0,0,0,0) 70%);
  }
  .rule {
    position: absolute; left: 0; right: 0; top: 186px; height: 2px;
    background: var(--lime);
  }
  .contact {
    position: absolute; right: 46px; top: 218px; text-align: right;
    font-family: "Open Sans", sans-serif; color: var(--lime);
  }
  .contact__name { font-weight: 700; font-size: 20px; margin-bottom: 14px; }
  .contact__line {
    display: flex; justify-content: flex-end; align-items: center; gap: 12px;
    font-size: 20px; margin-bottom: 12px;
  }
  .contact__line svg { width: 26px; height: 22px; fill: var(--lime); }

  .band {
    position: absolute; left: 0; right: 0; bottom: 0; height: 108px;
    background: linear-gradient(90deg, var(--silver-dark) 0%, var(--silver-mid) 22%, var(--silver-light) 40%, var(--silver-mid) 58%, var(--silver-dark) 78%, var(--silver-light) 100%);
  }
  .card--front .band { height: 104px; }
  .credentials {
    position: absolute; left: 40px; right: 20px; top: 28px;
    display: flex; align-items: center; gap: 26px;
    font-family: "Open Sans", sans-serif; font-size: 19px; color: var(--lime);
  }
  .tick { width: 22px; height: 18px; stroke: var(--lime); fill: none; stroke-width: 4; stroke-linecap: round; stroke-linejoin: round; }

  .services {
    position: absolute; left: 52px; top: 36px; list-style: none;
    font-family: "Old Standard TT", serif; font-size: 26px; color: var(--lime);
  }
  .services li { display: flex; align-items: center; gap: 24px; height: 42px; }
  .services .tick { width: 26px; height: 20px; }

  .thanks {
    position: absolute; left: 101px; top: 30px;
    font-family: "Old Standard TT", serif; font-style: italic;
    font-size: 28px; color: var(--lime);
  }
  .builders {
    position: absolute; left: 574px; top: 317px; width: 147px; height: 90px;
    background: var(--card); border: 4px solid var(--silver-light); border-radius: 8px;
    outline: 2px solid var(--silver-dark); outline-offset: -8px;
    display: flex; align-items: center; justify-content: center; text-align: center;
    font-family: "Old Standard TT", serif; font-weight: 700; font-size: 20px;
    line-height: 1.3; color: var(--lime);
  }
</style>
</head>
<body>
  <section class="card card--front">
    <div class="brand">
      <span class="brand__mark"></span>
      <span class="brand__name">Brensdale Electrical</span>
    </div>
    <p class="tagline">Professional cost effective soloutions.</p>
    <div class="glow"></div>
    <div class="rule"></div>
    <div class="contact">
      <p class="contact__name">GERALD PILWORTHY</p>
      <p class="contact__line">
        <svg viewBox="0 0 26 20" aria-hidden="true"><path d="M0 0h26v20H0z M2 2v1l11 8 11-8V2z"/></svg>
        brensdaleelectrical@mailvox.com.au
      </p>
      <p class="contact__line">
        <svg viewBox="0 0 24 24" aria-hidden="true"><path d="M6.6 10.8a15 15 0 0 0 6.6 6.6l2.2-2.2c.3-.3.7-.4 1-.2 1.1.4 2.3.6 3.6.6.6 0 1 .4 1 1V20c0 .6-.4 1-1 1A17 17 0 0 1 3 4c0-.6.4-1 1-1h3.5c.6 0 1 .4 1 1 0 1.3.2 2.5.6 3.6.1.3 0 .7-.2 1z"/></svg>
        0417302951
      </p>
    </div>
    <div class="band">
      <div class="credentials">
        <span>Lic No. 58120 AC</span>
        <svg class="tick" viewBox="0 0 22 18" aria-hidden="true"><path d="M3 7l7 8L20 3"/></svg>
        <span>Lic No. l293417</span>
        <svg class="tick" viewBox="0 0 22 18" aria-hidden="true"><path d="M3 7l7 8L20 3"/></svg>
        <span>ABN 37216058814</span>
      </div>
    </div>
  </section>

  <section class="card card--back">
    <ul class="services">
      <li><svg class="tick" viewBox="0 0 22 18" aria-hidden="true"><path d="M3 7l7 8L20 3"/></svg>Real estate and Commercial maintenance</li>
      <li><svg class="tick" viewBox="0 0 22 18" aria-hidden="true"><path d="M3 7l7 8L20 3"/></svg>New home and renovation rewires and upgrades</li>
      <li><svg class="tick" viewBox="0 0 22 18" aria-hidden="true"><path d="M3 7l7 8L20 3"/></svg>Split system air conditioning</li>
      <li><svg class="tick" viewBox="0 0 22 18" aria-hidden="true"><path d="M3 7l7 8L20 3"/></svg>Floor heat</li>
      <li><svg class="tick" viewBox="0 0 22 18" aria-hidden="true"><path d="M3 7l7 8L20 3"/></svg>TV phone data</li>
      <li><svg class="tick" viewBox="0 0 22 18" aria-hidden="true"><path d="M3 7l7 8L20 3"/></svg>Smoke detectors</li>
      <li><svg class="tick" viewBox="0 0 22 18" aria-hidden="true"><path d="M3 7l7 8L20 3"/></svg>Lighting systems</li>
    </ul>
    <div class="band">
      <p class="thanks">Thank you for your business!</p>
    </div>
    <div class="builders">BUILDERS<br>WELCOME</div>
  </section>
</body>
</html>
```